Continuing Professional Development Seminars
Power Point Template
• 11 juin 2011 15:52 rubenqol
thanks Velmoro
• 9 juin 2011 11:07 Velmoro
congrats your first project :)
• 9 juin 2011 02:48 tkvolaris
rubenqol - can you please upload a new draft that has the following slides:
1 - The title slide from draft#15 (I think this might be exactly the same in all subsequent drafts)
2 - The content slide from draft#15
3 - The content slide from draft#66
4 - The content slide from draft#68
5 - The last slide from draft#69
6 - The last slide from draft#15
I would like to see both of the end slides in the same draft.
Thanks.
• 7 juin 2011 08:20 tkvolaris
Thank you to all the designers who have submitted designs to date. The quality of the work is outstanding and is making the decision difficult.
I am still considering ALL the designs and will probably make a final decision soon. However, the designs that seem to stand out at the moment include (in no particular order) draft#50/draft#72, draft#15 (and the variations), draft#62 and draft#54.
• 6 juin 2011 06:31 tkvolaris
Draft#15 – can you please make the following changes:
1. Replace the last slide with a variant of the first slide. This new slide should be the same as the first slide, but with the following changes:
• The colours of the main background graphic should be reversed – so that becomes a red graphic with a blue stipe (instead of a blue graphic with a red stripe).
• Change the text - “Welcome to our Presentation” to “Thank you”.
• Change the white text (location and date) to the contact details you currently have on the last slide.
2. Can we try three small variations to the header on the content slides? Firstly, can you make the line under the presentation header about an inch smaller (so that it doesn’t go all the way to the logo). Secondly, can you please do a variant that reverses the logo and the header title (so that the logo is on the right and the presentation title is on the left). Thirdly, can you try a variant that doesn’t have the presentation header at all – only the logo? I would prefer having a look at all three slides to see how it looks. Thanks.
• 2 juin 2011 06:02 tkvolaris
Some of the recent designs have been very good. I particularly like the very bold graphical styles on the front pages whilst I prefer the more minimalist approach to the content slides.
I know that I said previously to try using our logo as a background watermark. However, on second thoughts I don’t think it really works. The watermarks are OK on the first slides, but on the content slides it is very distracting.
So far, my favourite designs are draft#15 and drafts#25-26. However, many of the designs have things I like or don’t like. Specifically,
• Draft#25 and Draft #26 – These designs are very effective. A bold front page and simple content pages. I think we would need to lose the watermarks on the content pages, but otherwise, these designs are on the right track.
• Draft#23 – I like the footer design of each content slide. Very simple and elegant.
• Draft#15 – perhaps my favourite design so far. Good bold first slide. The content slides are also good – maybe a little too busy as the moment?
• Draft#9 and Draft#10 – The first slides in these designs are very good. I like the strong bold designs. The content pages don’t really work – too much graphical background and not enough white space for content. One thing I like about these designs is the reverse colours of the background on the final slides.
Some of the other designs have similar good and bad points. However, I think I would be repeating myself if I discussed each one.
In summary, I like the first slides that are bold and emphasise our brand. The content slides should be simple, elegant and consistent.
• 31 mai 2011 19:56 tkvolaris
When I was looking through other projects on this website, there is one that I found that seems to be very effective. The project name is "Brisk Lanterns PowerPoint Template" and the design is draft#39.
I am not suggesting that I want a copy or a redraft of this design. It is just an example of something that I like.
• 31 mai 2011 19:47 tkvolaris
I like the designs that are creatively using the "swirls" on our logo. The first pages in draft#9 and draft#10 are interesting. I also didn't mind the first page in draft#11 (but note that it has been withdrawn?).
I think the logo needs to be more subtle on the content pages - maybe in the bottom right corner? Also maybe could use the logo as a watermark? Draft#4 uses a watermark, but being in the middle of the page, it might be a little distracting.

```html
<!DOCTYPE html>
<html lang="en">
<head>
<meta charset="utf-8">
<title>ARVEN Seminar Template Slides</title>
<link href="https://fonts.googleapis.com/css2?family=Libre+Baskerville:wght@400;700&display=swap" rel="stylesheet">
<style>
  :root {
    --stage: #000000;
    --slide-top: #ffffff;
    --slide-bottom: #dcdcdc;
    --brand-navy: #1c2f73;
    --brand-blue: #1f4fb3;
    --brand-blue-deep: #123a8f;
    --brand-red: #e2262b;
    --text-grey: #7a7a7a;
    --text-dark: #4a4a4a;
    --heading-blue: #2a5bbf;
    --grid: #d0d0d0;
  }
  * { margin: 0; padding: 0; box-sizing: border-box; }
  html, body { width: 1200px; height: 902px; overflow: hidden; background: var(--stage); }
  body { position: relative; font-family: "Libre Baskerville", serif; }

  .slide {
    position: absolute;
    overflow: hidden;
    background: radial-gradient(ellipse at 50% 35%, var(--slide-top) 40%, var(--slide-bottom) 100%);
  }
  .slide--title-a { left: 98px; top: 68px; width: 470px; height: 310px; }
  .slide--chart { left: 605px; top: 68px; width: 498px; height: 310px; }
  .slide--list { left: 98px; top: 415px; width: 470px; height: 422px; }
  .slide--title-b { left: 605px; top: 450px; width: 498px; height: 387px; }

  .wave { position: absolute; left: 0; bottom: 0; width: 100%; }

  .brand-name {
    position: absolute;
    font-family: "Libre Baskerville", serif;
    font-weight: 700;
    color: var(--brand-navy);
    letter-spacing: 1px;
    white-space: nowrap;
  }
  .brand-name--hero { font-size: 46px; left: 50%; transform: translateX(-50%); }
  .brand-name--small { font-size: 11px; }

  .closing {
    position: absolute;
    left: 0; width: 100%;
    display: flex; justify-content: center; align-items: center;
  }
  .closing__thanks {
    color: var(--text-grey);
    text-transform: uppercase;
    text-align: right;
    line-height: 1.1;
    padding-right: 12px;
    border-right: 1px solid #a8a8a8;
  }
  .closing__presenter { padding-left: 12px; color: var(--text-grey); }
  .closing__name { text-transform: uppercase; line-height: 1.1; }
  .closing__role { text-transform: uppercase; letter-spacing: 1px; color: #9a9a9a; }
  .closing__url {
    position: absolute; left: 0; width: 100%;
    text-align: center; color: #8a8a8a; letter-spacing: 4px; font-style: normal;
  }

  .slide-heading {
    position: absolute; left: 0; width: 100%;
    text-align: center; color: var(--text-dark); text-transform: uppercase;
  }
  .slide-heading__title { font-size: 15px; letter-spacing: 0.5px; }
  .slide-heading__sub { font-size: 5.5px; letter-spacing: 1px; margin-top: 2px; color: #777; }

  .group { margin-bottom: 9px; }
  .group__label { font-size: 6.5px; font-weight: 700; color: var(--heading-blue); margin-bottom: 2px; }
  .group__text { font-size: 4.8px; line-height: 1.45; color: #888; }

  .chart { position: absolute; left: 16px; top: 88px; width: 210px; height: 120px; }
  .chart-notes { position: absolute; left: 262px; top: 74px; width: 196px; }

  .list-columns { position: absolute; left: 36px; top: 88px; width: 400px; display: flex; gap: 36px; }
  .list-columns > div { flex: 1; }
</style>
</head>
<body>

<!-- Title slide (closing variant A) -->
<section class="slide slide--title-a">
  <div class="brand-name brand-name--hero" style="top:70px;">ARVEN</div>
  <div class="closing" style="top:176px;">
    <div class="closing__thanks" style="font-size:13px;">Thank you for<br>your attention</div>
    <div class="closing__presenter">
      <div class="closing__name" style="font-size:13px;">Presenter Name</div>
      <div class="closing__role" style="font-size:6px;">Designation</div>
    </div>
  </div>
  <address class="closing__url" style="top:216px; font-size:6.5px;">www.arven.com.au</address>
  <svg class="wave" height="95" viewBox="0 0 500 100" preserveAspectRatio="none" aria-hidden="true">
    <defs>
      <linearGradient id="blueA" x1="0" y1="0" x2="0" y2="1">
        <stop offset="0" stop-color="#2d63c9"/><stop offset="1" stop-color="#0f3485"/>
      </linearGradient>
    </defs>
    <path d="M0,52 C160,95 330,75 500,40 L500,100 L0,100Z" fill="url(#blueA)"/>
    <path d="M0,44 C160,88 330,66 500,28 L500,40 C330,76 160,96 0,52Z" fill="#ffffff"/>
    <path d="M0,36 C150,80 320,58 500,14 L500,30 C330,66 160,86 0,44Z" fill="var(--brand-red)"/>
    <path d="M0,70 C170,108 340,86 500,56" fill="none" stroke="#ffffff" stroke-width="1.5" opacity="0.8"/>
  </svg>
</section>

<!-- Content slide with chart -->
<section class="slide slide--chart">
  <div class="brand-name brand-name--small" style="left:50%; transform:translateX(-50%); top:18px;">ARVEN</div>
  <div class="slide-heading" style="top:34px;">
    <div class="slide-heading__title">Sample of Content List</div>
    <div class="slide-heading__sub">Description in this line</div>
  </div>
  <svg class="chart" viewBox="0 0 210 120" aria-label="Bar chart">
    <g stroke="var(--grid)" stroke-width="0.6">
      <line x1="10" y1="10" x2="205" y2="10"/><line x1="10" y1="30" x2="205" y2="30"/>
      <line x1="10" y1="50" x2="205" y2="50"/><line x1="10" y1="70" x2="205" y2="70"/>
      <line x1="10" y1="90" x2="205" y2="90"/>
    </g>
    <line x1="10" y1="110" x2="205" y2="110" stroke="#999" stroke-width="0.8"/>
    <line x1="10" y1="5" x2="10" y2="110" stroke="#999" stroke-width="0.8"/>
    <rect x="26" y="72" width="12" height="38" fill="var(--brand-blue)"/>
    <rect x="56" y="20" width="12" height="90" fill="var(--brand-blue)"/>
    <rect x="86" y="36" width="12" height="74" fill="var(--brand-blue)"/>
    <rect x="116" y="60" width="12" height="50" fill="var(--brand-red)"/>
    <rect x="146" y="46" width="12" height="64" fill="var(--brand-red)"/>
    <rect x="176" y="76" width="12" height="34" fill="var(--brand-blue)"/>
  </svg>
  <div class="chart-notes">
    <div class="group"><div class="group__label">Group 01</div><div class="group__text">Short notes on the seminar topic go here, with key points for members and a brief summary of the session outcome for all.</div></div>
    <div class="group"><div class="group__label">Group 02</div><div class="group__text">Short notes on the seminar topic go here, with key points for members and a brief summary of the session outcome for all.</div></div>
    <div class="group"><div class="group__label">Group 03</div><div class="group__text">Short notes on the seminar topic go here, with key points for members and a brief summary of the session outcome for all.</div></div>
    <div class="group"><div class="group__label">Group 04</div><div class="group__text">Short notes on the seminar topic go here, with key points for members and a brief summary of the session outcome for all.</div></div>
    <div class="group"><div class="group__label">Group 05</div><div class="group__text">Short notes on the seminar topic go here, with key points for members and a brief summary of the session outcome for all.</div></div>
  </div>
  <svg class="wave" height="48" viewBox="0 0 500 100" preserveAspectRatio="none" aria-hidden="true">
    <path d="M0,40 C160,80 330,70 500,30 L500,100 L0,100Z" fill="#ffffff" opacity="0.85"/>
    <path d="M0,30 C160,68 330,58 500,16 L500,28 C330,70 160,80 0,40Z" fill="var(--brand-red)"/>
    <path d="M0,60 C170,95 330,85 500,50 L500,100 L0,100Z" fill="var(--brand-blue-deep)"/>
  </svg>
  <div class="brand-name brand-name--small" style="left:340px; bottom:12px; font-size:7px;">ARVEN</div>
</section>

<!-- Content slide with text list -->
<section class="slide slide--list">
  <div class="brand-name brand-name--small" style="left:50%; transform:translateX(-50%); top:20px;">ARVEN</div>
  <div class="slide-heading" style="top:38px;">
    <div class="slide-heading__title">Sample of Content List</div>
    <div class="slide-heading__sub">Description in this line</div>
  </div>
  <div class="list-columns">
    <div>
      <div class="group"><div class="group__label">Group 01</div><div class="group__text">Short notes on the seminar topic go here, with key points for members and a brief summary of the session outcome for all.</div></div>
      <div class="group"><div class="group__label">Group 02</div><div class="group__text">Short notes on the seminar topic go here, with key points for members and a brief summary of the session outcome for all.</div></div>
      <div class="group"><div class="group__label">Group 03</div><div class="group__text">Short notes on the seminar topic go here, with key points for members and a brief summary of the session outcome for all.</div></div>
      <div class="group"><div class="group__label">Group 04</div><div class="group__text">Short notes on the seminar topic go here, with key points for members and a brief summary of the session outcome for all.</div></div>
    </div>
    <div>
      <div class="group"><div class="group__label">Group 05</div><div class="group__text">Short notes on the seminar topic go here, with key points for members and a brief summary of the session outcome for all.</div></div>
      <div class="group"><div class="group__label">Group 06</div><div class="group__text">Short notes on the seminar topic go here, with key points for members and a brief summary of the session outcome for all.</div></div>
      <div class="group"><div class="group__label">Group 07</div><div class="group__text">Short notes on the seminar topic go here, with key points for members and a brief summary of the session outcome for all.</div></div>
      <div class="group"><div class="group__label">Group 08</div><div class="group__text">Short notes on the seminar topic go here, with key points for members and a brief summary of the session outcome for all.</div></div>
    </div>
  </div>
  <svg class="wave" height="80" viewBox="0 0 500 100" preserveAspectRatio="none" aria-hidden="true">
    <path d="M0,40 C160,80 330,70 500,30 L500,100 L0,100Z" fill="#ffffff" opacity="0.85"/>
    <path d="M0,30 C160,68 330,58 500,16 L500,28 C330,70 160,80 0,40Z" fill="var(--brand-red)"/>
    <path d="M0,60 C170,95 330,85 500,50 L500,100 L0,100Z" fill="var(--brand-blue-deep)"/>
  </svg>
  <div class="brand-name brand-name--small" style="left:222px; bottom:48px; font-size:7px;">ARVEN</div>
</section>

<!-- Title slide (closing variant B) -->
<section class="slide slide--title-b">
  <div class="brand-name brand-name--hero" style="top:90px; font-size:50px;">ARVEN</div>
  <div class="closing" style="top:198px;">
    <div class="closing__thanks" style="font-size:14px;">Thank you for<br>your attention</div>
    <div class="closing__presenter">
      <div class="closing__name" style="font-size:14px;">Presenter Name</div>
      <div class="closing__role" style="font-size:6.5px;">Designation</div>
    </div>
  </div>
  <address class="closing__url" style="top:242px; font-size:7px;">www.arven.com.au</address>
  <svg class="wave" height="105" viewBox="0 0 500 100" preserveAspectRatio="none" aria-hidden="true">
    <defs>
      <linearGradient id="blueB" x1="0" y1="0" x2="0" y2="1">
        <stop offset="0" stop-color="#2d63c9"/><stop offset="1" stop-color="#0f3485"/>
      </linearGradient>
    </defs>
    <path d="M0,28 C170,70 330,60 500,48 L500,100 L0,100Z" fill="url(#blueB)"/>
    <path d="M0,22 C170,62 330,52 500,40 L500,48 C330,60 170,70 0,28Z" fill="#ffffff"/>
    <path d="M0,14 C170,54 330,44 500,30 L500,40 C330,52 170,62 0,22Z" fill="var(--brand-red)"/>
    <path d="M0,50 C170,92 330,80 500,70" fill="none" stroke="#ffffff" stroke-width="1.5" opacity="0.8"/>
  </svg>
</section>

</body>
</html>
```